Medical equipment business looking for professional, unique business card

We need a business card design for a durable medical equipment company. We are small but would like our cards to express that we are much bigger. We focus on braces (back, knee, wrist, etc) but also do crutches, rollators, wheelchairs- basically medical equipment that gets you going and back in Action. Our colors are blue and green and our logo has an arrow and use of a "spine". We'd like to express professionalism while being unique.

Industry/Entity Type

Medical Equipment

Contact Information for Business Card

Professional feel but unique. Memorable.

Font styles to use
Serif
Sans Serif
Other font styles liked:
• verdana

Requirements
Must have
• card holders cell#, business phone#, fax#, email, website address, business address, logo
Nice to have
• use of medical/healthcare related descriptive words, items, look
Should not have
• the wrong colors or cartoon characters.

```html
<!DOCTYPE html>
<html lang="en">
<head>
<meta charset="utf-8">
<title>Stridewell – Business Card</title>
<link rel="stylesheet" href="https://fonts.googleapis.com/css2?family=Montserrat:wght@400;600;700&display=swap">
<style>
  :root {
    --bg: #dfe2e5;
    --navy: #0c4a72;
    --navy-deep: #083a5b;
    --green: #6cc24a;
    --cream: #f2f0e6;
    --ink: #1d3f5c;
    --tag-blue: #1e7fb8;
    --white: #f4f6f4;
  }
  * { margin: 0; padding: 0; box-sizing: border-box; }
  html, body { width: 1200px; height: 786px; overflow: hidden; }
  body {
    background: var(--bg);
    font-family: "Montserrat", sans-serif;
    position: relative;
  }
  .card {
    position: absolute;
    top: 250px;
    width: 500px;
    height: 286px;
    border-radius: 16px;
    overflow: hidden;
    box-shadow: 0 10px 28px rgba(0,0,0,.18);
  }
  .card--front { left: 70px; background: var(--cream); }
  .card--back {
    left: 630px;
    background: linear-gradient(160deg, #125a86 0%, var(--navy) 55%, var(--navy-deep) 100%);
  }
  .front-swoosh { position: absolute; inset: 0; }

  .brand { position: absolute; }
  .brand__name {
    font-weight: 600;
    letter-spacing: .5px;
    line-height: 1;
  }
  .brand__tag {
    font-weight: 400;
    line-height: 1;
    margin-top: 6px;
    border-bottom: 2px solid var(--green);
    padding-bottom: 4px;
    display: inline-block;
  }
  .card--front .brand { left: 34px; top: 34px; }
  .card--front .brand__name { font-size: 38px; color: var(--ink); }
  .card--front .brand__tag { font-size: 12px; color: var(--tag-blue); }

  .card--back .brand {
    left: 0; right: 0; top: 100px; text-align: center;
  }
  .card--back .brand__name { font-size: 48px; color: var(--white); }
  .card--back .brand__tag { font-size: 14px; color: var(--green); margin-top: 8px; }

  .contact {
    position: absolute;
    left: 268px;
    top: 128px;
    color: var(--ink);
  }
  .contact__name { font-weight: 700; font-size: 15px; letter-spacing: .5px; text-transform: uppercase; }
  .contact__role { font-size: 11px; margin-top: 2px; margin-bottom: 12px; }
  .contact__list { list-style: none; }
  .contact__list li {
    display: flex; align-items: center; gap: 7px;
    font-size: 11px; height: 16px;
  }
  .icon { width: 12px; height: 12px; flex: none; }
  .contact__address { font-size: 11px; margin-top: 8px; line-height: 1.45; }
</style>
</head>
<body>

  <section class="card card--front" aria-label="Card front">
    <svg class="front-swoosh" viewBox="0 0 500 286" preserveAspectRatio="none" aria-hidden="true">
      <path d="M0 140 C 90 190, 200 220, 250 286 L0 286 Z" fill="var(--navy)"/>
      <path d="M0 130 C 100 175, 215 205, 262 286" fill="none" stroke="var(--green)" stroke-width="7"/>
      <path d="M0 152 C 95 198, 200 226, 246 286" fill="none" stroke="var(--green)" stroke-width="2"/>
    </svg>

    <div class="brand">
      <div class="brand__name">Stridewell</div>
      <div class="brand__tag">Durable Medical Equipment</div>
    </div>

    <div class="contact">
      <div class="contact__name">Jordan Maylen</div>
      <div class="contact__role">General Manager</div>
      <ul class="contact__list">
        <li>
          <svg class="icon" viewBox="0 0 12 12"><rect width="12" height="12" rx="2" fill="var(--green)"/><path d="M3.5 2.5h1.5l.7 2-1 .8a5 5 0 0 0 2 2l.8-1 2 .7v1.5c0 .5-.4.8-.9.8A6.5 6.5 0 0 1 2.7 3.4c0-.5.3-.9.8-.9z" fill="#fff"/></svg>
          555-014-2210
        </li>
        <li>
          <svg class="icon" viewBox="0 0 12 12"><rect width="12" height="12" rx="2" fill="var(--green)"/><rect x="3" y="2.5" width="6" height="3" fill="#fff"/><rect x="2.5" y="6" width="7" height="3.5" rx=".5" fill="#fff"/></svg>
          555-014-2211
        </li>
        <li>
          <svg class="icon" viewBox="0 0 12 12"><rect width="12" height="12" rx="2" fill="var(--green)"/><rect x="2.5" y="3.5" width="7" height="5" fill="#fff"/><path d="M2.5 3.5 6 6.5l3.5-3" fill="none" stroke="var(--green)" stroke-width=".8"/></svg>
          info@stridewell.com
        </li>
        <li>
          <svg class="icon" viewBox="0 0 12 12"><rect width="12" height="12" rx="2" fill="var(--green)"/><circle cx="6" cy="6" r="3.3" fill="none" stroke="#fff" stroke-width=".9"/><path d="M2.7 6h6.6M6 2.7v6.6" stroke="#fff" stroke-width=".8"/></svg>
          www.stridewell.com
        </li>
      </ul>
      <div class="contact__address">48 Harbor Lane, Suite 310<br>Fairview MA 01920</div>
    </div>
  </section>

  <section class="card card--back" aria-label="Card back">
    <div class="brand">
      <div class="brand__name">Stridewell</div>
      <div class="brand__tag">Durable Medical Equipment</div>
    </div>
  </section>

</body>
</html>
```